Flooring & Interior Design showroom

Just bought this business- Kestrel Lane Flooring & Interiors. Love our logo (we are on Kestrel Lane )and colors
Forest green, gold and black
Love that the back lists everything we do. We no longer have plenotilex but need to add in LVP/ SPC and need to take out vantor shadehub logo at the bottom and use the quib logo instead (maybe? open to suggestions)

Not in love with our cards- I want a higher end look
I hate the gradient poop color we have now.
Would love if they were all black - maybe or ??
or had a foil or embossing?

```html
<!DOCTYPE html>
<html lang="en">
<head>
<meta charset="utf-8">
<title>Kestrel Lane Flooring &amp; Interiors – Business Cards</title>
<link href="https://fonts.googleapis.com/css2?family=Figtree:wght@400;500;600&display=swap" rel="stylesheet">
<style>
  :root {
    --forest: #0c3b2f;
    --forest-deep: #0a2a22;
    --gold: #d4bf7a;
    --gold-soft: rgba(212, 191, 122, 0.55);
    --ink: #151515;
    --paper: #ffffff;
    --backdrop: #e3e5e5;
    --bullet: #2f6b4d;
  }
  * { box-sizing: border-box; margin: 0; padding: 0; }
  html, body {
    width: 1200px; height: 900px; overflow: hidden;
    background: var(--backdrop);
    font-family: "Figtree", Arial, sans-serif;
  }
  .card {
    position: absolute; top: 39px;
    width: 468px; height: 815px;
    border-radius: 40px;
  }
  .card::after {
    content: ""; position: absolute; inset: 14px;
    border-radius: 30px; border: 1px solid var(--gold-soft);
    pointer-events: none;
  }
  .card--front { left: 133px; background: var(--paper); color: var(--ink); }
  .card--back { left: 614px; background: linear-gradient(160deg, var(--forest) 0%, var(--forest-deep) 100%); color: #fff; }

  .brand { position: absolute; left: 0; right: 0; top: 78px; height: 180px; }
  .brand__mark {
    position: absolute; left: 62px; top: 16px;
    width: 50px; height: 50px; border-radius: 50%;
  }
  .brand__name {
    position: absolute; left: 118px; top: 58px;
    font-size: 37px; font-weight: 600; letter-spacing: 0.5px; white-space: nowrap;
  }
  .brand__tag {
    position: absolute; left: 122px; top: 112px;
    font-size: 17px; font-weight: 600; letter-spacing: 1.6px; text-transform: uppercase; white-space: nowrap;
  }
  .card--front .brand__mark { background: var(--forest); }
  .card--front .brand__name { color: var(--forest); }
  .card--front .brand__tag { color: var(--forest); }
  .card--back .brand { top: 120px; }
  .card--back .brand__mark { background: var(--gold); }
  .card--back .brand__name, .card--back .brand__tag { color: var(--gold); }

  .front-contact {
    position: absolute; top: 322px; left: 0; right: 0;
    text-align: center; font-size: 21px; line-height: 32.5px;
  }
  .services {
    position: absolute; top: 446px; list-style: none;
    font-size: 20.5px; line-height: 32.3px;
  }
  .services--a { left: 55px; }
  .services--b { left: 234px; }
  .services li { position: relative; padding-left: 22px; white-space: nowrap; }
  .services li::before {
    content: ""; position: absolute; left: 0; top: 12px;
    width: 11px; height: 11px; border-radius: 50%; background: var(--bullet);
  }

  .person { position: absolute; top: 333px; left: 0; right: 0; text-align: center; }
  .person__name { font-size: 35px; font-weight: 500; letter-spacing: 0.5px; line-height: 40px; color: var(--gold); }
  .person__role { font-size: 20px; line-height: 26px; }
  .address {
    position: absolute; top: 421px; left: 0; right: 0;
    text-align: center; font-size: 20px; line-height: 29px; font-style: normal;
  }
  .contact-icons {
    position: absolute; top: 508px; left: 0; right: 0;
    display: flex; justify-content: center; gap: 30px;
  }
  .contact-icons svg { width: 28px; height: 28px; fill: var(--gold); }
  .contact-list {
    position: absolute; top: 547px; left: 0; right: 0;
    list-style: none; text-align: center; font-size: 20px; line-height: 38.8px;
  }
  .partners {
    position: absolute; top: 746px; left: 0; right: 0;
    display: flex; justify-content: center; gap: 52px;
    font-size: 24px; line-height: 30px; font-weight: 600; color: var(--gold);
  }
</style>
</head>
<body>

<section class="card card--front" aria-label="Card front">
  <div class="brand">
    <span class="brand__mark"></span>
    <span class="brand__name">Kestrel Lane</span>
    <span class="brand__tag">Flooring &amp; Interiors</span>
  </div>

  <div class="front-contact">
    <p>Home Town Service Since 1979</p>
    <p>555.210.0142</p>
    <p>www.kestrellaneflooring.com</p>
  </div>

  <ul class="services services--a">
    <li>Area Rugs</li><li>Blinds</li><li>Carpet</li><li>Cork</li><li>Hardwood</li>
    <li>Laminate</li><li>Sheers</li><li>Valances</li><li>Vinyl</li>
  </ul>
  <ul class="services services--b">
    <li>Bed Spreads</li><li>Draperies</li><li>Fabric</li><li>Motorized Shades</li>
    <li>Pillows</li><li>Shutters</li><li>Upholstery</li><li>Verticals</li><li>LVP/ SPC</li>
  </ul>
</section>

<section class="card card--back" aria-label="Card back">
  <div class="brand">
    <span class="brand__mark"></span>
    <span class="brand__name">Kestrel Lane</span>
    <span class="brand__tag">Flooring &amp; Interiors</span>
  </div>

  <div class="person">
    <p class="person__name">DANA WHITLOCK</p>
    <p class="person__role">Owner/ Designer</p>
  </div>

  <address class="address">314 Kestrel Lane,<br>Cedar Bay CA 95512</address>

  <div class="contact-icons" aria-hidden="true">
    <svg viewBox="0 0 24 24"><path d="M6.6 10.8a15.1 15.1 0 0 0 6.6 6.6l2.2-2.2a1 1 0 0 1 1-.25 11.4 11.4 0 0 0 3.6.57 1 1 0 0 1 1 1V20a1 1 0 0 1-1 1A17 17 0 0 1 3 4a1 1 0 0 1 1-1h3.5a1 1 0 0 1 1 1c0 1.25.2 2.45.57 3.6a1 1 0 0 1-.25 1z"/></svg>
    <svg viewBox="0 0 24 24"><path d="M2 9c0-3 4-5 10-5s10 2 10 5v1h-5V8H7v2H2zM6 11h12l3 9H3zm4 2v2h1v-2zm3 0v2h1v-2zm-3 3v2h1v-2zm3 0v2h1v-2z"/></svg>
    <svg viewBox="0 0 24 24"><path d="M7 3h10v5H7zM4 9h16a2 2 0 0 1 2 2v6h-4v4H6v-4H2v-6a2 2 0 0 1 2-2zm4 6v4h8v-4z"/></svg>
    <svg viewBox="0 0 24 24"><path d="M2 5h20v14H2zm2 2v.4l8 5.2 8-5.2V7zm0 2.8V17h16V9.8l-8 5.2z"/></svg>
  </div>

  <ul class="contact-list">
    <li>Store 555.210.0142</li>
    <li>Cell 555-318-4027</li>
    <li>Faz 555.604.7731</li>
    <li>ben@kestrellaneflooring.com</li>
    <li>CA Lic # 408163</li>
  </ul>

  <div class="partners">
    <span>Marlowe Shades</span>
    <span>quib</span>
  </div>
</section>

</body>
</html>
```